QUIVL Systems website

We need a website design using much of the information on the QUIVL flyer (attached) we just had a PixelMarsh designer create. We'd like a WordPress Site, no need for a shopping cart attached to it. It should have an About us page, Book titles page, a blog page, Membership and Navigators pages contact us and privacy policy and terms of services.

Coding

Coded - Design and coding required

```html
<!DOCTYPE html>
<html lang="en">
<head>
<meta charset="utf-8">
<title>QUIVL Systems</title>
<link rel="stylesheet" href="https://fonts.googleapis.com/css2?family=Nunito+Sans:wght@400;600;700;800&family=Montserrat:wght@500;600;700&display=swap">
<style>
:root{
  --blue:#2f5b97;
  --blue-deep:#284f86;
  --yellow:#f6b91c;
  --ink:#333a44;
  --muted:#6f7680;
  --line:#e3e5e8;
  --grey-bg:#f1f2f4;
  --white:#ffffff;
}
*{box-sizing:border-box;margin:0;padding:0}
html,body{width:1200px;height:3327px;overflow:hidden}
body{font-family:"Nunito Sans",Arial,sans-serif;color:var(--ink);background:var(--white);position:relative}
.brand-mark{color:var(--yellow)}
.tm{font-size:.55em;vertical-align:super}

/* hero */
.hero{position:absolute;left:0;top:0;width:1200px;height:566px;background:linear-gradient(120deg,#4f6478 0%,#3c4e63 35%,#6b7b8c 60%,#3a4656 100%)}
.hero-photo{position:absolute;inset:0;background:linear-gradient(90deg,rgba(30,45,65,.55) 0%,rgba(30,45,65,.15) 55%,rgba(20,30,45,.35) 100%)}
.topbar-call{position:absolute;right:153px;top:20px;color:var(--white);font:600 14px "Montserrat",sans-serif;display:flex;align-items:center;gap:6px}
.logo{position:absolute;left:153px;top:34px;color:var(--white);font:700 38px "Montserrat",sans-serif;letter-spacing:2px}
.nav{position:absolute;left:370px;top:62px;display:flex;gap:0;font:600 11.5px "Montserrat",sans-serif;color:var(--white);letter-spacing:.5px}
.nav a{color:inherit;text-decoration:none;position:absolute;white-space:nowrap}
.nav .active{color:var(--yellow)}
.login-btn{position:absolute;left:949px;top:60px;width:98px;height:25px;background:var(--yellow);color:var(--white);font:700 10px "Montserrat",sans-serif;display:flex;align-items:center;justify-content:center;letter-spacing:.5px}
.hero-title{position:absolute;left:153px;top:244px;color:var(--white);font:800 29px/34px "Nunito Sans",sans-serif}
.btn-outline{display:inline-flex;align-items:center;justify-content:center;border:1.5px solid var(--yellow);color:var(--yellow);font:700 9.5px "Montserrat",sans-serif;letter-spacing:.6px;height:33px;background:transparent}
.hero .btn-outline{position:absolute;left:153px;top:374px;width:131px}
.dots{position:absolute;left:1014px;top:292px;display:flex;flex-direction:column;gap:8px}
.dots span{width:12px;height:12px;border:1.5px solid var(--white);border-radius:50%}
.dots span.on{background:var(--white)}
.hero-arrow{position:absolute;left:592px;top:548px}

/* welcome */
.welcome{position:absolute;left:0;top:566px;width:1200px;height:344px;background:var(--blue);color:var(--white);text-align:center}
.welcome h2{position:absolute;left:0;right:0;top:66px;font:800 28px "Nunito Sans",sans-serif}
.welcome h3{position:absolute;left:0;right:0;top:102px;font:700 21px "Nunito Sans",sans-serif}
.welcome p{position:absolute;left:235px;width:730px;top:148px;font:400 13px/21px "Nunito Sans",sans-serif}
.welcome .btn-outline{position:absolute;left:536px;top:248px;width:128px}

/* membership */
.member-head{position:absolute;left:0;right:0;top:964px;text-align:center}
.member-head h2{font:700 28px "Nunito Sans",sans-serif;color:var(--ink)}
.member-head h3{font:600 22px "Nunito Sans",sans-serif;color:var(--ink);margin-top:2px}
.b{color:var(--blue)}
.feature-img{position:absolute;width:419px;height:282px}
.feature-text{position:absolute;width:420px}
.feature-text h4{font:600 20px "Nunito Sans",sans-serif;color:var(--ink);margin-bottom:18px}
.feature-text h4 .b{font-family:"Montserrat",sans-serif;font-weight:600;letter-spacing:1px}
.ticks{list-style:none}
.ticks li{position:relative;padding-left:22px;font:400 13px/18px "Nunito Sans",sans-serif;color:var(--muted);margin-bottom:6px}
.ticks li::before{content:"";position:absolute;left:0;top:2px;width:12px;height:12px;border:1.3px solid #8e949b;border-radius:50%}
.ticks li::after{content:"";position:absolute;left:4px;top:5px;width:5px;height:3px;border-left:1.3px solid #8e949b;border-bottom:1.3px solid #8e949b;transform:rotate(-45deg)}
.btn-solid{display:inline-flex;align-items:center;justify-content:center;background:var(--yellow);color:var(--white);font:700 9.5px "Montserrat",sans-serif;letter-spacing:.6px;height:33px}
.feature-text .btn-outline,.feature-text .btn-solid{width:145px;margin-top:14px}
.divider{position:absolute;left:153px;width:894px;top:2068px;height:1px;background:var(--line)}

/* consultation */
.consult{position:absolute;left:0;right:0;top:2128px;text-align:center}
.consult h2{font:700 27px "Nunito Sans",sans-serif;color:var(--ink)}
.consult h3{font:600 26px/34px "Nunito Sans",sans-serif;color:var(--blue);width:620px;margin:22px auto 0}
.consult .vline{width:2px;height:62px;background:var(--blue);margin:38px auto 0}
.consult .btn-blue{display:inline-flex;align-items:center;justify-content:center;width:113px;height:34px;background:var(--blue);color:var(--white);font:700 9.5px "Montserrat",sans-serif;letter-spacing:.6px;margin-top:34px}

/* blogs */
.blogs{position:absolute;left:0;top:2473px;width:1200px;height:499px;background:var(--grey-bg)}
.blogs h2{position:absolute;left:153px;top:56px;font:600 27px "Nunito Sans",sans-serif}
.blogs h2 .b{font-family:"Montserrat",sans-serif;letter-spacing:1px}
.blogs .btn-solid{position:absolute;left:917px;top:60px;width:130px}
.card{position:absolute;top:115px;width:282px;height:322px;background:var(--white);text-align:center}
.card .thumb{height:162px}
.card p{font:400 15px/21px "Nunito Sans",sans-serif;color:var(--ink);padding:28px 40px 0;height:128px}
.card p.hover{color:var(--blue);text-decoration:underline}
.card time{font:700 9.5px "Montserrat",sans-serif;color:var(--blue);letter-spacing:.5px}
.card time.hl{color:var(--yellow)}

/* footer */
.footer{position:absolute;left:0;top:2972px;width:1200px;height:355px;background:var(--blue-deep);color:var(--white);text-align:center}
.footer .flogo{position:absolute;left:0;right:0;top:60px;font:700 42px "Montserrat",sans-serif;letter-spacing:3px}
.footer .contact{position:absolute;left:0;right:0;top:172px;font:600 13.5px "Montserrat",sans-serif;color:var(--white)}
.footer .contact .y{color:var(--yellow)}
.socials{position:absolute;left:0;right:0;top:216px;display:flex;justify-content:center;gap:14px}
.socials span{width:35px;height:35px;border-radius:50%;border:1.5px solid var(--yellow)}
.socials span.on{background:var(--yellow)}
.copy{position:absolute;left:0;right:0;top:279px;font:400 12px "Nunito Sans",sans-serif}
.copy u{text-decoration:underline}
.to-top{position:absolute;left:1073px;top:158px}
</style>
</head>
<body>

<header class="hero">
  <div class="hero-photo" role="img" aria-label="Photo of two colleagues working together at a desk with a laptop and notes"></div>
  <div class="topbar-call">Call Us:
    <svg width="13" height="13" viewBox="0 0 24 24"><path fill="#fff" d="M6.6 10.8a15 15 0 0 0 6.6 6.6l2.2-2.2a1 1 0 0 1 1-.25 11.4 11.4 0 0 0 3.6.57 1 1 0 0 1 1 1V20a1 1 0 0 1-1 1A17 17 0 0 1 3 4a1 1 0 0 1 1-1h3.5a1 1 0 0 1 1 1c0 1.25.2 2.45.57 3.57a1 1 0 0 1-.25 1z"/></svg>
    555-014-2290</div>
  <div class="logo">QUIVL</div>
  <nav class="nav">
    <a class="active" style="left:0">HOME</a>
    <a style="left:71px">ABOUT US</a>
    <a style="left:167px">MEMBERSHIP</a>
    <a style="left:284px">NAVIGATORS</a>
    <a style="left:397px">BLOG</a>
    <a style="left:464px">CONTACT US</a>
  </nav>
  <div class="login-btn">LOGIN</div>
  <h1 class="hero-title">How <span class="brand-mark">QUIVL<span class="tm">™</span></span><br>Accelerates Your Business<br>Growth!</h1>
  <a class="btn-outline">CONTACT US</a>
  <div class="dots"><span></span><span class="on"></span><span></span><span></span></div>
  <svg class="hero-arrow" width="16" height="22" viewBox="0 0 16 22"><path d="M8 0v18M2 12l6 7 6-7" stroke="#f6b91c" stroke-width="2.2" fill="none"/></svg>
</header>

<section class="welcome">
  <h2>Welcome to <span class="brand-mark">QUIVL<span class="tm">™</span></span></h2>
  <h3>Created By Entrepreneurs For Entrepreneurs</h3>
  <p>A team of 7 successful entrepreneurs put their heads together in an effort to help improve the statistics on how many small businesses succeed. After tapping into the great minds of business thought leaders* from around the globe, they developed the first comprehensive program for small businesses (up to $5M revenues) and packaged it into a simple, affordable, sustainable membership model. And QUIVL™ was born!</p>
  <a class="btn-outline">DISCOVER MORE</a>
</section>

<section class="membership">
  <div class="member-head">
    <h2>Become a <span class="b">QUIVL</span><span class="tm">™</span> Member Today</h2>
    <h3>And you Will Receive...</h3>
  </div>

  <div class="feature-img" style="left:153px;top:1060px;background:linear-gradient(135deg,#8a8f96,#5d636b 55%,#a7a9ad)" role="img" aria-label="Photo of a coaching session with a mentor speaking to a group"></div>
  <div class="feature-text" style="left:628px;top:1078px">
    <h4><span class="b">QUIVL</span><span class="tm">™</span> Coaching</h4>
    <ul class="ticks">
      <li>Coaching for you and your leadership team</li>
      <li>Launch pad, monthly and quarterly touchpoints, annual planning</li>
      <li>Continuous learning model</li>
      <li>All QUIVL coaches are successful million-dollar entrepreneurs (our Navigators)</li>
    </ul>
    <a class="btn-outline">CONTACT US</a>
  </div>

  <div class="feature-text" style="left:153px;top:1420px">
    <h4><span class="b">QUIVL</span><span class="tm">™</span> Structure</h4>
    <ul class="ticks">
      <li>Structured program that ensures focus, productivity and accountability.</li>
      <li>Robust collection of simple, streamlined tools and processes</li>
      <li>QUIVL Strategy Stack – for clarity and alignment</li>
    </ul>
    <a class="btn-solid">BECOME A MEMBER</a>
  </div>
  <div class="feature-img" style="left:628px;top:1392px;background:radial-gradient(circle at 50% 45%,#4a4d52,#222428 75%)" role="img" aria-label="Photo of pins on a dark board linked by red thread"></div>

  <div class="feature-img" style="left:153px;top:1722px;background:linear-gradient(120deg,#b9a58a,#6d7d8e 45%,#2e3f57 75%,#8b8f86)" role="img" aria-label="Photo of a person analysing dashboards on a desktop monitor"></div>
  <div class="feature-text" style="left:628px;top:1758px">
    <h4><span class="b">QUIVL</span><span class="tm">™</span> Resources</h4>
    <ul class="ticks">
      <li>Pre-packaged business processes</li>
      <li>Simplified business templates and forms</li>
      <li>Online, self-paced learning library</li>
      <li>Technology platform for tracking and accountability</li>
    </ul>
    <a class="btn-outline">SIGN UP NOW!</a>
  </div>
  <div class="divider"></div>
</section>

<section class="consult">
  <h2>Get a <span class="b">QUIVL</span><span class="tm">™</span> Free Consultation</h2>
  <h3>A Simple, Comprehensive Coaching System for Small Businesses</h3>
  <div class="vline"></div>
  <a class="btn-blue">LETS TALK</a>
</section>

<section class="blogs">
  <h2><span class="b">QUIVL</span><span class="tm">™</span> Blogs</h2>
  <a class="btn-solid">VIEW ALL</a>
  <article class="card" style="left:153px">
    <div class="thumb" style="background:linear-gradient(135deg,#2b3546,#4d5563 60%,#8a7a62)" role="img" aria-label="Photo of a hand stacking wooden blocks on a desk"></div>
    <p>There are many work variations of passages lorem majority have...</p>
    <time>29-SEP-2018</time>
  </article>
  <article class="card" style="left:459px">
    <div class="thumb" style="background:linear-gradient(135deg,#6e7278,#a3a6aa 50%,#55595f)" role="img" aria-label="Photo of darts hitting the centre of a target"></div>
    <p class="hover">There are many work variations of passages lorem majority have...</p>
    <time class="hl">30-SEP-2018</time>
  </article>
  <article class="card" style="left:765px">
    <div class="thumb" style="background:linear-gradient(135deg,#7b8ea8,#c9b79e 50%,#5d6f88)" role="img" aria-label="Photo of a team celebrating around a table"></div>
    <p>There are many work variations of passages lorem majority have...</p>
    <time>01-OCT-2018</time>
  </article>
</section>

<footer class="footer">
  <div class="flogo">QUIVL</div>
  <div class="contact"><span class="y">Call Us:</span> 555-014-2290, &nbsp;<span class="y">E.</span> hello@quivl.example</div>
  <div class="socials"><span></span><span class="on"></span><span></span><span></span></div>
  <div class="copy">© 2018 QUIVL. All Rights Reserved. &nbsp;<u>Terms &amp; Conditions</u> &nbsp;|&nbsp; Privacy Policy</div>
  <svg class="to-top" width="22" height="26" viewBox="0 0 22 26"><path d="M2 24L11 2l9 22M6 15h10" stroke="#f6b91c" stroke-width="2.2" fill="none"/></svg>
</footer>

</body>
</html>
```